Hairdressing Salon called; Velvet Tress. Style Lives Here

Velvet Tress
We Love Hair
418 Penrose Lane Birch Vale
5183742
Business card not to fussy.
I would like it to be a Black background with White and/or Grey lettering.

I really like the business card attached, so if the front looked like this I would be really happy, but would also like my address and phone number on the front.

On the back I would like two options of
1: reward card; buy any Haircare product over $20 on any visit and on the tenth product receive a complimentry Treatment and
2: appointment times and date

Industry/Entity Type

Business

Contact Information for Business Card

Velvet Tress
We Love Hair
5183742
418 Penrose Lane, Birch Vale
This must all be included on the front of the card

Font styles to use
Serif
Decorative
Script

Colors
1b1b1b
757575
ffffff

Requirements
Must have
• My phone number and address
Should not have
• Pictures on the front

```html
<!DOCTYPE html>
<html lang="en">
<head>
<meta charset="utf-8">
<title>Velvet Tress – Business Card</title>
<link rel="stylesheet" href="https://fonts.googleapis.com/css2?family=Cormorant+Garamond:ital,wght@1,500&family=Pinyon+Script&family=Arimo&display=swap">
<style>
  :root {
    --paper: #1b1b1b;
    --ink: #ffffff;
    --muted: #b8b8b8;
    --band: #757575;
    --rule: #9a9a9a;
    --ornament: #757575;
  }
  * { margin: 0; padding: 0; box-sizing: border-box; }
  html, body {
    width: 1200px;
    height: 326px;
    overflow: hidden;
    background: var(--paper);
  }
  .card {
    position: relative;
    width: 1200px;
    height: 326px;
    background: var(--paper);
    color: var(--ink);
  }
  .edge-rule {
    position: absolute;
    left: 25px;
    top: 0;
    width: 8px;
    height: 100%;
    background: var(--rule);
  }
  .side-band {
    position: absolute;
    left: 38px;
    top: 0;
    width: 80px;
    height: 100%;
    background: var(--band);
  }
  .band-name {
    position: absolute;
    left: 42px;
    top: 18px;
    width: 72px;
    height: 110px;
    display: flex;
    align-items: center;
    justify-content: center;
  }
  .band-name span {
    display: block;
    transform: rotate(-90deg);
    white-space: nowrap;
    font-family: "Cormorant Garamond", serif;
    font-style: italic;
    font-weight: 500;
    font-size: 22px;
    color: var(--ink);
  }
  .scroll-border {
    position: absolute;
    left: 119px;
    top: 0;
    width: 22px;
    height: 100%;
    background: linear-gradient(90deg, var(--paper), var(--ornament) 50%, var(--paper));
  }
  .brand {
    position: absolute;
    left: 178px;
    top: 14px;
    font-family: "Cormorant Garamond", serif;
    font-style: italic;
    font-weight: 500;
    font-size: 56px;
    line-height: 1;
    letter-spacing: 0.5px;
    color: var(--ink);
  }
  .tagline {
    position: absolute;
    left: 200px;
    top: 80px;
    width: 328px;
    text-align: center;
    font-family: "Pinyon Script", cursive;
    font-size: 21px;
    line-height: 24px;
    color: var(--muted);
  }
  .contact {
    position: absolute;
    left: 200px;
    top: 118px;
    width: 328px;
    text-align: center;
    font-family: "Arimo", Arial, sans-serif;
    font-style: normal;
    font-size: 20px;
    line-height: 26px;
    color: var(--ink);
  }
  .offers {
    position: absolute;
    left: 730px;
    top: 108px;
    width: 470px;
    list-style: none;
    font-family: "Arimo", Arial, sans-serif;
    font-size: 20.5px;
    line-height: 26px;
    color: var(--ink);
  }
  .offers li {
    display: grid;
    grid-template-columns: 25px 1fr;
    white-space: nowrap;
  }
</style>
</head>
<body>
  <main class="card">
    <div class="edge-rule"></div>
    <div class="side-band"></div>
    <div class="band-name"><span>Velvet Tress</span></div>
    <div class="scroll-border" role="img" aria-label="Vertical border of small decorative scrolls"></div>

    <h1 class="brand">Velvet Tress</h1>
    <p class="tagline">We Love Hair</p>

    <address class="contact">
      418 Penrose Lane Birch Vale<br>
      5183742
    </address>

    <ol class="offers">
      <li><span>1:</span><span>Reward card; buy any Haircare product over<br>$20 on any visit and on the tenth product<br>receive a complimentry Treatment and</span></li>
      <li><span>2:</span><span>Appointment times and date</span></li>
    </ol>
  </main>
</body>
</html>
```